Website re-design wedding music business

I need my wordpress wedding music website redesigned. I'm a wedding pianist and also provide duo/trio entertainment with other musicians and looking for an overhaul of my wordpress site.

Website: tollykessing.com.au

Target Market(s)

brides; engaged couples

Industry/Entity Type

Wedding

Number of Pages Required

5+ page

Colors

Designer to choose colors to be used in the design.

Requirements
Must have
• I'm looking to overhaul my website which is looking rather tired after 4 years. It is functional but not inviting to visitors. Initially my website started out as a solo piano player providing music for wedding. It is gradually growing now where brides can book
• 1) Solo Piano
• 2) Duo (any combination of Piano / Cello / Vocalist / Violin)
• 3) Trio (any combination of Piano/ Cello /Vocalist / Violin)
• in future it may increase to 4 / 5 /6 piece bands so that needs to be taken into account for the future growth where I'll recruit other musicians.
• Some other functionality I'd like to see
• - Visitors want a calendar to know availability of musicians
• - Automatically providing enquiry price & discount (if applicable)
• - Automating the booking form process (manual) - There's a PDF form I send to the customer after we go back/forth on email on songs/price etc but if more of it could be automated online that would be great. If move to online it would be good to be able to override the set prices with a custom price and also providing a payment gateway
• More Flexibility on pricing - customer selects type of artists they want and it calculates a price based on who they have chosen whether it is a ceremony or canapes or reception (or combination of any). Extra transport fee is added if >50km out of Melbourne.
• How would you re-design this website. Imagine you are a bride/groom looking to book wedding music services. I would love to see some concepts .
• Please indicate any other fees required for your submission and level of support post this competition. I would like this to be an on-going relationship.
Nice to have
• I'd preferably like the website to be in wordpress as I've been familiar with it over time and can do basic updates in the back end. Happy for other suggestions if you can convince me I should move away from wordpress.

```html
<!DOCTYPE html>
<html lang="en">
<head>
<meta charset="utf-8">
<title>Tolly Kessing – Wedding Pianist</title>
<link rel="stylesheet" href="https://fonts.googleapis.com/css2?family=Lato:wght@400;700;900&family=Open+Sans:wght@400;600&display=swap">
<style>
:root{
  --black:#000;
  --ink:#111;
  --text:#444;
  --muted:#777;
  --white:#fff;
  --grey-band:#ebebeb;
  --card:#fafafa;
  --orange:#e8562a;
  --cal-bg:rgba(20,20,20,.88);
  --cal-line:rgba(255,255,255,.12);
  --badge:#8a8a8a;
}
*{margin:0;padding:0;box-sizing:border-box}
html,body{width:1200px;height:2624px;overflow:hidden}
body{position:relative;background:var(--white);font-family:'Open Sans',Arial,sans-serif;color:var(--text)}
.abs{position:absolute}

/* header */
.site-header{position:absolute;left:0;top:0;width:1200px;height:100px;background:var(--white)}
.brand{position:absolute;display:flex;align-items:center;gap:10px;font-family:'Lato',Arial,sans-serif;font-weight:900;font-size:24px;color:var(--ink);letter-spacing:.5px}
.brand .dot{width:60px;height:60px;border-radius:50%;background:var(--ink)}
.brand.light{color:var(--white)}
.brand.light .dot{background:var(--white)}
.top-nav{position:absolute;left:684px;top:30px;width:381px;height:37px;border:1px solid #ddd;display:flex;align-items:center;font-size:10px;font-weight:600;color:var(--ink)}
.top-nav a{padding:0 14px;height:100%;display:flex;align-items:center;text-decoration:none;color:inherit}
.top-nav a.active{background:var(--black);color:var(--white)}
.main-nav{position:absolute;left:0;top:100px;width:1200px;height:38px;background:var(--black);display:flex;justify-content:space-between;align-items:center;padding:0 133px 0 131px;font-size:11.5px;color:var(--white);font-family:'Open Sans',Arial,sans-serif}

/* hero */
.hero{position:absolute;left:0;top:138px;width:1200px;height:675px}
.hero-photo{position:absolute;inset:0;background:linear-gradient(180deg,#3d4a2a 0%,#56623a 40%,#6e6548 75%,#d9d9d9 84%,#f2f2f2 100%)}
.hero-title{position:absolute;left:761px;top:46px;font-family:'Lato',Arial,sans-serif;font-weight:900;font-size:29px;line-height:38px;color:var(--white);letter-spacing:.5px}
.calendar{position:absolute;left:764px;top:147px;width:261px;background:var(--cal-bg);color:var(--white);font-family:'Lato',Arial,sans-serif}
.calendar .month{height:32px;display:flex;align-items:center;justify-content:center;font-size:13px;font-weight:700}
.calendar .grid{display:grid;grid-template-columns:repeat(7,1fr)}
.calendar .dow{height:20px;font-size:9px;font-weight:700;display:flex;align-items:center;justify-content:center;background:#000}
.calendar .day{height:35px;border-right:1px solid var(--cal-line);border-bottom:1px solid var(--cal-line);display:flex;align-items:center;justify-content:center;font-size:12px}
.calendar .day.off{color:#666}
.calendar .day.today span{background:var(--orange);width:26px;height:26px;display:flex;align-items:center;justify-content:center}
.book-now{position:absolute;left:764px;top:410px;width:261px;height:64px;background:var(--orange);color:var(--white);font-family:'Lato',Arial,sans-serif;font-weight:900;font-size:29px;display:flex;align-items:center;justify-content:center}
.hero-arrow{position:absolute;top:253px;width:48px;height:48px}

/* packages */
.package{position:absolute;top:855px;width:295px}
.package .photo{height:222px;background:linear-gradient(160deg,#4a5a34,#2f3524 60%,#bdbdb6)}
.package .label{margin-top:16px;font-family:'Lato',Arial,sans-serif;font-size:19px;color:var(--ink)}
.package .label b{font-weight:900}

/* sections */
.band{position:absolute;left:0;width:1200px}
.band.grey{background:var(--grey-band)}
.section-title{position:absolute;left:0;width:1200px;text-align:center;font-family:'Lato',Arial,sans-serif;font-weight:900;font-size:24px;color:var(--ink)}

.event{position:absolute;width:226px;height:152px;background:var(--card);padding:26px 18px 0 33px}
.event h3{font-family:'Lato',Arial,sans-serif;font-weight:900;font-size:11.5px;line-height:17px;color:var(--ink);text-transform:uppercase}
.event .date{font-size:9.5px;color:var(--text);margin-top:5px}
.event .time{position:absolute;left:33px;bottom:30px;font-size:12px;color:var(--ink);display:flex;align-items:center;gap:6px}
.btn-dark{position:absolute;left:516px;top:1662px;width:168px;height:47px;background:#222;color:var(--white);font-size:12px;font-weight:600;display:flex;align-items:center;justify-content:center;font-family:'Open Sans',Arial,sans-serif}

.track{position:absolute;top:1910px;width:201px;height:53px;border:1.5px solid #cfcfcf;background:var(--white);display:flex;align-items:center;padding:0 12px;font-size:12px;color:var(--ink)}
.track .play{width:11px;height:11px;border-radius:50%;background:var(--ink);margin-right:10px;position:relative}
.track .len{margin-left:auto;font-size:8px;color:var(--muted)}

.quote{position:absolute;left:255px;top:2166px;width:690px;text-align:center;font-size:13px;line-height:24px;color:#555}
.quote-mark{position:absolute;font-family:Georgia,serif;font-size:56px;color:#c8c8c8;line-height:1}
.author{position:absolute;left:0;top:2291px;width:1200px;text-align:center;font-family:'Lato',Arial,sans-serif;font-weight:900;font-size:13px;color:var(--ink)}
.badge{position:absolute;top:2357px;width:60px;height:60px;border-radius:50%}

/* footer */
.site-footer{position:absolute;left:0;top:2475px;width:1200px;height:149px;background:var(--black);color:var(--white)}
.follow{position:absolute;left:476px;top:70px;font-size:10px}
.social{position:absolute;top:63px;width:30px;height:30px;border-radius:50%;background:#3b5b8f}
.copyright{position:absolute;right:135px;top:70px;font-size:10px}
</style>
</head>
<body>

<header class="site-header">
  <div class="brand" style="left:131px;top:18px"><span class="dot"></span>TOLLYKESSING</div>
  <nav class="top-nav">
    <a class="active">HOME</a><a>ABOUT TOLLY</a><a>FAQS</a><a>CONTACT</a><a>PHOTO FEED</a>
  </nav>
</header>
<nav class="main-nav">
  <span>EVENTS</span><span>MUSIC</span><span>VIDEO</span><span>REPERTOIRE</span><span>PRICES</span><span>GALLERY</span><span>TESTIMONIALS</span><span>BUY CD</span><span>SUPPLIERS</span><span>HIRE BABY GRAND PIANO</span>
</nav>

<section class="hero">
  <div class="hero-photo" role="img" aria-label="Pianist in a dark suit playing a white grand piano under park trees, above a strip of piano keys"></div>
  <h1 class="hero-title">WEDDING PIANIST<br>EVENT PIANIST</h1>
  <div class="calendar">
    <div class="month">JULY 2017</div>
    <div class="grid">
      <div class="dow">SU</div><div class="dow">MO</div><div class="dow">TU</div><div class="dow">WE</div><div class="dow">TH</div><div class="dow">FR</div><div class="dow">SA</div>
      <div class="day"></div><div class="day"></div><div class="day"></div><div class="day"></div><div class="day"></div><div class="day"></div><div class="day">1</div>
      <div class="day">2</div><div class="day off">3</div><div class="day">4</div><div class="day">5</div><div class="day">6</div><div class="day">7</div><div class="day">8</div>
      <div class="day">9</div><div class="day">10</div><div class="day">11</div><div class="day">12</div><div class="day off">13</div><div class="day">14</div><div class="day">15</div>
      <div class="day">16</div><div class="day off">17</div><div class="day">18</div><div class="day">19</div><div class="day today"><span>20</span></div><div class="day off">21</div><div class="day off">22</div>
      <div class="day">23</div><div class="day">24</div><div class="day off">25</div><div class="day">26</div><div class="day off">27</div><div class="day off">28</div><div class="day off">29</div>
      <div class="day">30</div><div class="day off">31</div><div class="day"></div><div class="day"></div><div class="day"></div><div class="day"></div><div class="day"></div>
    </div>
  </div>
  <svg class="abs" style="left:770px;top:181px" width="250" height="14" viewBox="0 0 250 14"><path d="M8 3 4 7 8 11M242 3 246 7 242 11" stroke="#fff" stroke-width="1.5" fill="none"/></svg>
  <div class="book-now">BOOK NOW</div>
  <svg class="hero-arrow" style="left:70px" viewBox="0 0 48 48"><circle cx="24" cy="24" r="22" fill="#000" stroke="#fff" stroke-width="2"/><path d="M27 17 20 24 27 31" stroke="#fff" stroke-width="2" fill="none"/></svg>
  <svg class="hero-arrow" style="left:1074px" viewBox="0 0 48 48"><circle cx="24" cy="24" r="22" fill="#000" stroke="#fff" stroke-width="2"/><path d="M21 17 28 24 21 31" stroke="#fff" stroke-width="2" fill="none"/></svg>
</section>

<div class="package" style="left:135px"><div class="photo" role="img" aria-label="Solo pianist at a white piano outdoors"></div><p class="label"><b>SOLO</b> PIANO</p></div>
<div class="package" style="left:453px"><div class="photo" role="img" aria-label="Pianist with a cellist in a garden"></div><p class="label"><b>DUO</b> PIANO</p></div>
<div class="package" style="left:770px"><div class="photo" role="img" aria-label="Keyboard player with cellist and vocalist"></div><p class="label"><b>TRIO</b> PIANO</p></div>

<section class="band grey" style="top:1167px;height:605px"></section>
<h2 class="section-title" style="top:1219px">EVENTS</h2>

<article class="event" style="left:138px;top:1296px"><h3>Private Event – Harrowdene (TBC</h3><p class="date">July 30, Sunday</p><p class="time">◷ 2:00 pm - 3:00 pm</p></article>
<article class="event" style="left:371px;top:1296px"><h3>Wedding Ceremony &amp; Canapes – Fernleigh Estate</h3><p class="date">August 17, Sunday</p><p class="time">◷ 3:30 pm - 6:00 pm</p></article>
<article class="event" style="left:604px;top:1296px"><h3>Private Event – Harrowdene (TBC)</h3><p class="date">July 30, Sunday</p><p class="time">◷ 2:00 pm - 3:00 pm</p></article>
<article class="event" style="left:838px;top:1296px"><h3>Wedding Ceremony – St Aldric's Chapel (Piano/Vocal) TBC</h3><p class="date">October 2017</p><p class="time">◷ 8:00 am - 5:00 pm</p></article>
<article class="event" style="left:138px;top:1457px"><h3>Wedding Reception Willowmere Lodge Piano /Vocal TBC</h3><p class="date">July 30, Sunday</p><p class="time">◷ 8:00 am - 10:00 pm</p></article>
<article class="event" style="left:371px;top:1457px"><h3>Wedding Ceremony Elmcourt (Piano / Cello) TBC</h3><p class="date">August 17, Sunday</p><p class="time">◷ 3:30 pm - 6:00 pm</p></article>
<article class="event" style="left:604px;top:1457px"><h3>Wedding Ceremony – Piano/Cello</h3><p class="date">July 30, Sunday</p><p class="time">◷ 12:45 pm - 1:45 pm</p></article>
<article class="event" style="left:838px;top:1457px"><h3>Wedding Ceremony – St Aldric's Chapel (Piano/Vocal) TBC</h3><p class="date">October 2017</p><p class="time">◷ 8:00 am - 5:00 pm</p></article>
<div class="btn-dark">VIEW MORE EVENTS</div>

<h2 class="section-title" style="top:1834px">MUSIC</h2>
<svg class="abs" style="left:128px;top:1929px" width="14" height="14" viewBox="0 0 14 14"><path d="M9 2 4 7 9 12" stroke="#111" stroke-width="2" fill="none"/></svg>
<div class="track" style="left:187px"><span class="play"></span>Lorem Ipsum is simp<span class="len">124k</span></div>
<div class="track" style="left:396px"><span class="play"></span>Lorem Ipsum is simp<span class="len">124k</span></div>
<div class="track" style="left:605px"><span class="play"></span>Lorem Ipsum is simp<span class="len">124k</span></div>
<div class="track" style="left:814px"><span class="play"></span>Lorem Ipsum is simp<span class="len">124k</span></div>
<svg class="abs" style="left:1055px;top:1929px" width="14" height="14" viewBox="0 0 14 14"><path d="M5 2 10 7 5 12" stroke="#111" stroke-width="2" fill="none"/></svg>

<section class="band grey" style="top:2029px;height:446px"></section>
<h2 class="section-title" style="top:2089px">TESTIMONIALS</h2>
<span class="quote-mark" style="left:215px;top:2136px">“</span>
<p class="quote">Tolly and Odessa (Cellist) played at our ceremony on 5th Nov 2016. They worked really well together and the music that they played was perfect. So many of my guests commented that the music was so good. Tolly was really easy to work with right from the first email to the actual day. We would definitely recommend them to anyone who needs a good pianist and cellist! Thanks Tolly and Odessa</p>
<span class="quote-mark" style="left:856px;top:2234px">”</span>
<svg class="abs" style="left:535px;top:2293px" width="14" height="14" viewBox="0 0 14 14"><path d="M9 2 4 7 9 12" stroke="#111" stroke-width="2" fill="none"/></svg>
<p class="author">PRIYA</p>
<svg class="abs" style="left:654px;top:2293px" width="14" height="14" viewBox="0 0 14 14"><path d="M5 2 10 7 5 12" stroke="#111" stroke-width="2" fill="none"/></svg>
<div class="badge" style="left:491px;background:#222"></div>
<div class="badge" style="left:572px;background:#c9a23a"></div>
<div class="badge" style="left:659px;background:#a9b0c4"></div>

<footer class="site-footer">
  <div class="brand light" style="left:131px;top:48px"><span class="dot"></span>TOLLYKESSING</div>
  <span class="follow">Follow us</span>
  <span class="social" style="left:539px"></span>
  <span class="social" style="left:578px"></span>
  <span class="social" style="left:617px"></span>
  <span class="social" style="left:655px"></span>
  <span class="social" style="left:690px"></span>
  <span class="copyright">Copyrights @ 2017 All Rights Reserved</span>
</footer>

</body>
</html>
```